Gentle Willow Pregnancy and Baby Massage

I need a web design for a new business, GENTLE WILLOW PREGNANCY AND BABY MASSAGE that I am in the process of setting up in the suburbs of Perth, Western Australia. The business is owned and operated by myself and my intention is to service Pregnant Mothers and Parents of Young Babies that would benefit from massage. I would like to have a "Home Page" and pages for "About Me", "Pregnancy Massage", "Baby Massage", a Pricing Page for Pregnancy Massage Sessions, a Pricing Page for Baby Massage Sessions, and a "Contact Me" page to allow clients to either contact me with queries or book available pregnancy massage sessions on a particular day of the week. I would also like a "News" page that would include articles I have written, news about new courses and a link to my Chatterlane page (yet to be set up). I would like to keep the colour schemes similar to my logo design colours. I need the design to be easy to follow and to appeal to a younger audience (20's to mid 30's).
The target audience is pregnant mothers-to-be wishing to receive massage treatments, and new parents and grandparents of small babies that would like to learn how to massage their babies.
The look and feel should be modern, professional, elegant and feminine.
I need the design to be in a standard format such that I can update the content by myself ( and does not need specialised software) as the company and business progresses.

Target Market(s)

Industry/Entity Type

Health And Wellness

Contact Information for Business Card

Card should have rounded edges. Design should have the same "feel" as the website. Contact Details of my business address, mobile phone, email and website should be included.

Coding

Coded - Design and coding required

Number of Pages Required

5+ page

Font styles to use
Script

Requirements
Must have
• Same colours as logo design. In cmyk system, the colours are: 20,60,0,0 which best result is tintora 681 and 40,40,0,0 which best result is tintora 2645. Card should include the logo design.

```html
<!DOCTYPE html>
<html lang="en">
<head>
<meta charset="utf-8">
<title>Gentle Willow Pregnancy and Baby Massage – Baby Massage Pricing</title>
<link rel="stylesheet" href="https://fonts.googleapis.com/css2?family=Questrial&family=Open+Sans:wght@400&display=swap">
<style>
  :root {
    --bar-dark: #3b3a3f;
    --footer-purple: #4e4775;
    --orchid: #a96bb1;
    --lavender: #8a7fc0;
    --blush: #f6e6ee;
    --blush-light: #fbf1f5;
    --ink: #2c2c2c;
    --grey-text: #8d8d8d;
    --rule: #d4d4d4;
    --white: #ffffff;
  }
  * { box-sizing: border-box; margin: 0; padding: 0; }
  html, body { width: 1200px; height: 2564px; overflow: hidden; background: var(--white); }
  body { position: relative; font-family: "Questrial", sans-serif; color: var(--ink); }
  h1, h2, h3 { font-weight: 400; }

  .top-bar { position: absolute; top: 0; left: 0; width: 1200px; height: 38px; background: var(--bar-dark); }
  .main-nav { position: absolute; top: 0; right: 132px; height: 38px; display: flex; gap: 30px; align-items: center; }
  .main-nav a { color: #e8e8e8; text-decoration: none; font-size: 13px; }
  .main-nav a.current { text-decoration: underline; text-underline-offset: 3px; }

  .header-waves { position: absolute; top: 38px; left: 0; }

  .brand-card {
    position: absolute; top: 0; left: 132px; width: 283px; height: 180px;
    background: var(--white); border-radius: 0 0 22px 22px;
    box-shadow: 0 3px 8px rgba(0,0,0,0.25);
  }
  .brand-card-inner {
    position: absolute; inset: 0 10px 10px 10px; border: 2px dashed #9a9a9a; border-top: none;
    border-radius: 0 0 16px 16px; display: flex; flex-direction: column; align-items: center; justify-content: center; gap: 8px;
  }
  .brand-dot { width: 34px; height: 34px; border-radius: 50%; background: var(--orchid); }
  .brand-name { font-size: 22px; color: var(--orchid); text-align: center; line-height: 1.2; }

  .block { position: absolute; left: 132px; width: 936px; }
  .page-title { left: 0; width: 1200px; text-align: center; font-size: 31px; color: var(--orchid); }
  .course-title { left: 0; width: 1200px; text-align: center; font-size: 32px; color: var(--lavender); }
  .course-intro { left: 0; width: 1200px; text-align: center; font-size: 18px; }
  .heading { font-size: 19px; }
  .body-text { font-size: 18px; line-height: 29px; }

  .feature-list { list-style: none; font-size: 14px; }
  .feature-list li { height: 30.5px; padding-left: 20px; position: relative; }
  .feature-list li::before { content: "›"; position: absolute; left: 0; top: -3px; font-size: 16px; }
  .sub-list { list-style: none; font-size: 14px; padding-left: 20px; }
  .sub-list li { height: 30px; }

  .fact { display: flex; font-size: 19px; color: var(--lavender); line-height: 28px; }
  .fact-label { width: 112px; display: flex; justify-content: space-between; }
  .fact-label span:last-child { margin-right: 14px; }
  .fact-value { flex: 1; }
  .fact.compact .fact-label { width: 72px; }

  .divider { position: absolute; left: 132px; width: 936px; height: 0; border-top: 2px solid var(--rule); }

  .session-name { font-size: 18px; line-height: 29px; }

  .site-footer { position: absolute; top: 2244px; left: 0; width: 1200px; height: 208px;
    background: linear-gradient(90deg, var(--blush), var(--blush-light) 50%, var(--blush)); }
  .cert-badge { position: absolute; left: 145px; top: 29px; width: 111px; height: 145px; border-radius: 50% 50% 12px 12px; background: #ecd9ea; border: 2px solid #c9a5cf; }
  .cert-text { position: absolute; left: 268px; top: 30px; font-size: 24px; line-height: 30px; color: var(--grey-text); }
  .cert-text .cert-org { color: var(--lavender); }
  .follow { position: absolute; left: 960px; top: 68px; width: 140px; text-align: center; font-size: 15px; color: var(--ink); }
  .follow-link { margin-top: 12px; display: flex; align-items: center; justify-content: center; gap: 8px; color: var(--footer-purple); font-size: 15px; }
  .follow-dot { width: 22px; height: 22px; border-radius: 50%; background: var(--footer-purple); }

  .base-bar { position: absolute; top: 2452px; left: 0; width: 1200px; height: 112px; background: var(--footer-purple);
    color: var(--white); font-family: "Open Sans", sans-serif; text-align: center; }
  .footer-nav { margin-top: 33px; font-size: 12px; }
  .footer-nav a { color: var(--white); text-decoration: none; }
  .footer-nav .sep { margin: 0 9px; }
  .copyright { margin-top: 10px; font-size: 11.5px; }
</style>
</head>
<body>

<div class="top-bar"></div>
<nav class="main-nav">
  <a href="#">Home</a><a href="#">About Me</a><a href="#">Pregnancy Massage</a><a href="#">Baby Massage</a><a href="#" class="current">Pricing</a><a href="#">News</a><a href="#">Contact Me</a>
</nav>

<svg class="header-waves" width="1200" height="150" viewBox="0 0 1200 150" aria-hidden="true">
  <rect x="0" y="0" width="1200" height="20" fill="#c8bee0"/>
  <path d="M0 0 H1200 V120 C1060 40 900 10 760 40 C600 80 450 110 300 70 C180 40 80 60 0 130 Z" fill="#c8bee0"/>
  <path d="M0 0 H1200 V60 C1080 20 950 -5 800 25 C640 60 480 95 320 55 C190 25 90 40 0 95 Z" fill="#b3a6d6"/>
  <path d="M700 0 H1200 V140 C1100 70 980 40 860 30 C800 25 740 20 700 0 Z" fill="#e6c3dc" opacity="0.85"/>
</svg>

<div class="brand-card">
  <div class="brand-card-inner">
    <span class="brand-dot"></span>
    <span class="brand-name">Gentle Willow<br>Pregnancy and Baby Massage</span>
  </div>
</div>

<h1 class="block page-title" style="top:253px">Baby Massage Sessions</h1>
<h2 class="block course-title" style="top:309px">Introductory Baby Massage Course</h2>
<p class="block course-intro" style="top:354px">This class teaches parents and carers the brief basics of Baby massage so they can get started at home.</p>

<section>
  <h3 class="block heading" style="top:407px">Included in this course:</h3>
  <ul class="block feature-list" style="top:451px">
    <li>Permission sequence</li>
    <li>Which Oils to Use</li>
    <li>When is the best time to massage your baby</li>
    <li>Contraindications (when not to massage)</li>
    <li>Basic massage techniques for:</li>
  </ul>
  <ul class="block sub-list" style="top:603px">
    <li>o Legs</li><li>o Abdomen</li><li>o Chest</li><li>o Back</li>
  </ul>
  <div class="block fact" style="top:740px"><div class="fact-label"><span>Duration</span><span>:</span></div><div class="fact-value">45-60 minutes</div></div>
  <div class="block fact" style="top:791px"><div class="fact-label"><span>Cost</span><span>:</span></div><div class="fact-value">Group booking – $30 per person (minimum of 3 parents and babies)<br>Private lesson – $75<br>Bring change mat and towel</div></div>
</section>

<div class="divider" style="top:936px"></div>

<section>
  <h3 class="block heading" style="top:998px">Colic relief course</h3>
  <p class="block body-text" style="top:1036px">This session is designed to focus on relief of colic, wind, constipation and reflux. The strokes used for relief will<br>be discussed and demonstrated, as well as general information about Baby massage and the use of<br>appropriate oils.</p>
  <div class="block fact" style="top:1139px"><div class="fact-label"><span>Duration</span><span>:</span></div><div class="fact-value">45-60 minutes</div></div>
  <div class="block fact" style="top:1190px"><div class="fact-label"><span>Cost</span><span>:</span></div><div class="fact-value">Group booking- $30 per person (minimum of 3 parents and babies)<br>Private lesson- $75<br>Bring change mat and towel</div></div>
</section>

<div class="divider" style="top:1334px"></div>

<section>
  <h3 class="block heading" style="top:1398px">Ante Natal Session</h3>
  <p class="block body-text" style="top:1435px">Basic massage techniques are demonstrated and practised on dolls provided, so that you can start to<br>massage your baby as soon as he/she is born.</p>
  <div class="block fact" style="top:1514px"><div class="fact-label"><span>Duration</span><span>:</span></div><div class="fact-value">60 minutes</div></div>
  <div class="block fact" style="top:1565px"><div class="fact-label"><span>Cost</span><span>:</span></div><div class="fact-value">Group booking- $30 per person<br>Private lesson $75</div></div>
</section>

<div class="divider" style="top:1679px"></div>

<section>
  <h3 class="block heading" style="top:1741px">Advanced Baby Massage (3 one-hour sessions)</h3>
  <p class="block session-name" style="top:1780px">Session 1</p>
  <p class="block body-text" style="top:1807px">This session covers, oils, permission sequence, contraindications for massage, massage strokes for legs, feet<br>and buttocks. When to massage and for how long</p>
  <p class="block session-name" style="top:1870px">Session 2</p>
  <p class="block body-text" style="top:1897px">This session covers baby’s daily cycle, benefits, body cues, strokes for abdominal and chest massage, and<br>touch relaxation.</p>
  <p class="block session-name" style="top:1959px">Session 3</p>
  <p class="block body-text" style="top:1986px">Face, arms and back. Lymphatic drainage. Review of strokes</p>
  <div class="block fact compact" style="top:2033px"><div class="fact-label"><span>Cost</span><span>:</span></div><div class="fact-value">$90 for 3 sessions (as part of a group session)<br>$150 for 2 private sessions</div></div>
  <p class="block body-text" style="top:2138px">(All the above courses include a small bottle of massage oil)</p>
</section>

<footer class="site-footer" role="img" aria-label="Soft pink footer backdrop">
  <div class="cert-badge" role="img" aria-label="Certification badge"></div>
  <p class="cert-text">Certified by<br><span class="cert-org">Little Touch<br>Learning</span><br>Network</p>
  <div class="follow">Follow us on
    <div class="follow-link"><span class="follow-dot"></span>Chatterlane</div>
  </div>
</footer>

<div class="base-bar">
  <p class="footer-nav"><a href="#">Home</a><span class="sep">|</span><a href="#">About Me</a><span class="sep">|</span><a href="#">Pregnancy Massage</a><span class="sep">|</span><a href="#">Baby Massage</a><span class="sep">|</span><a href="#">Pricing</a><span class="sep">|</span><a href="#">News</a><span class="sep">|</span><a href="#">Contact Me</a></p>
  <p class="copyright">Copyright © 2017 Gentle Willow Pregnancy &amp; Baby Massage. &nbsp;All rights reserved.</p>
</div>

</body>
</html>
```